stationary design

Marketing stationary. Nothing complicated please. My LOGO was designed here and I just want it attached to most of my stationary. I am not yet into Flyers and banners.
I have a consulting firm that is handling all other aspects of my business.
Thank you.

```html
<!DOCTYPE html>
<html lang="en">
<head>
<meta charset="utf-8">
<title>Letterhead &amp; Envelope Design</title>
<link rel="stylesheet" href="https://fonts.googleapis.com/css2?family=Gelasio:wght@400;500&family=Lora:ital,wght@0,400;0,500;1,400&display=swap">
<style>
  :root {
    --olive: #b2a245;
    --gold: #9c8a3c;
    --gold-dark: #8a7b40;
    --lime: #c3c23f;
    --navy: #06042a;
    --ink: #1d1b33;
    --heading: #3a3a3a;
    --paper: #ffffff;
    --faint: #efece0;
  }
  * { box-sizing: border-box; margin: 0; padding: 0; }
  html, body { width: 1200px; height: 1200px; overflow: hidden; }
  body { position: relative; background: var(--paper); font-family: "Lora", Georgia, serif; color: var(--ink); }

  .board-header { position: absolute; top: 0; left: 0; width: 1200px; height: 150px; text-align: center; color: var(--heading); font-family: "Gelasio", Georgia, serif; }
  .board-title { position: absolute; top: 30px; width: 100%; font-size: 35px; font-weight: 400; letter-spacing: 0.2px; }
  .board-spec { position: absolute; top: 76px; width: 100%; font-size: 22px; }

  .board { position: absolute; top: 150px; left: 0; width: 1200px; height: 1050px; background: var(--olive); }

  .label { position: absolute; font-family: "Gelasio", Georgia, serif; font-size: 22px; color: var(--heading); }

  .sheet { position: absolute; background: var(--paper); box-shadow: 0 1px 6px rgba(60,50,10,0.25); overflow: hidden; }

  .brand { position: absolute; display: flex; align-items: center; gap: 8px; }
  .brand-mark { background: var(--gold); }
  .brand-name { color: var(--gold); font-family: "Gelasio", Georgia, serif; font-weight: 500; line-height: 1.05; text-transform: uppercase; letter-spacing: 0.5px; }

  .contact { position: absolute; border-left: 1.5px solid var(--gold); font-family: "Lora", Georgia, serif; color: var(--ink); white-space: nowrap; }
  .contact b { color: var(--gold); font-weight: 500; margin-right: 4px; }

  .address { position: absolute; font-style: italic; color: var(--gold-dark); white-space: nowrap; }
  .tag-band { position: absolute; right: 0; background: linear-gradient(90deg, #a39345, #8a7c44); clip-path: polygon(5% 0, 100% 0, 100% 100%, 0 100%); color: #f4f0dc; font-style: italic; display: flex; align-items: center; justify-content: center; letter-spacing: 0.4px; }
  .base-rule { position: absolute; left: 0; bottom: 0; width: 100%; background: linear-gradient(90deg, var(--lime), var(--gold-dark)); }

  /* letterhead */
  .letterhead { left: 500px; top: 232px; width: 671px; height: 866px; }
  .letterhead .brand { left: 27px; top: 32px; }
  .letterhead .brand-mark { width: 40px; height: 40px; }
  .letterhead .brand-name { font-size: 20px; }
  .letterhead .contact { top: 44px; height: 31px; padding-left: 11px; font-size: 10.5px; line-height: 14px; }
  .letterhead .contact-phone { left: 320px; }
  .letterhead .contact-web { left: 436px; }
  .watermark { position: absolute; left: 200px; top: 260px; width: 250px; height: 250px; border-radius: 50%; background: var(--faint); opacity: 0.7; }
  .letterhead .address { left: 14px; top: 838px; font-size: 12.5px; }
  .letterhead .tag-band { top: 822px; width: 208px; height: 39px; font-size: 16px; padding-left: 10px; }
  .letterhead .base-rule { height: 5px; }

  /* envelopes */
  .envelope { left: 17px; width: 595px; height: 235px; }
  .envelope-front { top: 522px; }
  .envelope-back { top: 783px; }
  .envelope-front .brand { left: 25px; top: 16px; }
  .envelope-front .brand-mark { width: 26px; height: 26px; }
  .envelope-front .brand-name { font-size: 13px; }
  .envelope-front .contact { top: 21px; height: 24px; padding-left: 9px; font-size: 7px; line-height: 11px; }
  .envelope-front .contact-phone { left: 343px; }
  .envelope-front .contact-web { left: 438px; }
  .envelope-front .address { left: 15px; top: 210px; font-size: 9px; }
  .envelope-front .tag-band { top: 203px; width: 157px; height: 27px; font-size: 11px; padding-left: 8px; }
  .envelope-front .base-rule { height: 5px; }

  .flap-band { position: absolute; top: 0; left: 0; width: 100%; height: 56px; background: var(--navy); }
  .envelope-back .brand { left: 50%; top: 14px; transform: translateX(-50%); }
  .envelope-back .brand-mark { width: 26px; height: 26px; }
  .envelope-back .brand-name { font-size: 12px; }
</style>
</head>
<body>
  <header class="board-header">
    <h1 class="board-title">Letterhead &amp; Envelope Design- Mockup 1</h1>
    <p class="board-spec">Letterhead Size: 8.5in X 11.0in, Enevelope Size: 9.5in 4.125in &nbsp;|&nbsp; Template Guide: printkit.com</p>
  </header>

  <main class="board"></main>

  <section class="sheet letterhead" aria-label="Letterhead">
    <div class="brand">
      <span class="brand-mark"></span>
      <span class="brand-name">Hollis<br>Family Law</span>
    </div>
    <div class="contact contact-phone"><b>T:</b>905-555-0142<br><b>F:</b>905-555-0143</div>
    <div class="contact contact-web"><b>E:</b>legal.assistant@hollisfamilylaw.ca<br><b>W:</b>www.hollisfamilylaw.ca</div>
    <div class="watermark"></div>
    <p class="address">48 Maplecrest Court, Suite 310, Mississauga, Ontario, Canada, L5R 0A1</p>
    <div class="tag-band">Barristers &amp; Solicitors</div>
    <div class="base-rule"></div>
  </section>

  <p class="label" style="left:19px; top:478px;">Envelope - Front</p>

  <section class="sheet envelope envelope-front" aria-label="Envelope front">
    <div class="brand">
      <span class="brand-mark"></span>
      <span class="brand-name">Hollis<br>Family Law</span>
    </div>
    <div class="contact contact-phone"><b>T:</b>905-555-0142<br><b>F:</b>905-555-0143</div>
    <div class="contact contact-web"><b>E:</b>legal.assistant@hollisfamilylaw.ca<br><b>W:</b>www.hollisfamilylaw.ca</div>
    <p class="address">48 Maplecrest Court, Suite 310, Mississauga, Ontario, Canada, L5R 0A1</p>
    <div class="tag-band">Barristers &amp; Solicitors</div>
    <div class="base-rule"></div>
  </section>

  <section class="sheet envelope envelope-back" aria-label="Envelope back">
    <div class="flap-band"></div>
    <div class="brand">
      <span class="brand-mark"></span>
      <span class="brand-name">Hollis<br>Family Law</span>
    </div>
  </section>

  <p class="label" style="left:314px; top:1021px;">Envelope - Back</p>
</body>
</html>
```